Copper Wagon
ideas, energy & innovation
Can you also please upload drafts of the letter headed paper, compliments slips and invoice drafts for me to also look at!

```html
<!DOCTYPE html>
<html lang="en">
<head>
<meta charset="utf-8">
<title>Copper Wagon Stationery</title>
<link href="https://fonts.googleapis.com/css2?family=Open+Sans:wght@400;600;700&display=swap" rel="stylesheet">
<style>
:root{
  --bg:#e7e4e0;
  --paper:#ffffff;
  --ink:#3a3a3a;
  --muted:#8a8a8a;
  --rule:#cfcfcf;
  --blue:#1f7fd0;
  --blue-dark:#0f5ea8;
  --orange:#f07f12;
  --yellow:#f7c21b;
  --green:#6cb33f;
  --green-dark:#4f9a2a;
  --black:#1c1c1c;
}
*{box-sizing:border-box;margin:0;padding:0}
html,body{width:1200px;height:650px;overflow:hidden}
body{background:var(--bg);font-family:"Open Sans",Arial,sans-serif;color:var(--ink);position:relative}
.item{position:absolute;background:var(--paper);box-shadow:0 2px 6px rgba(0,0,0,.25)}
.logo{display:flex;align-items:center;gap:5px}
.logo-mark{width:14px;height:14px;border-radius:3px;background:var(--blue)}
.logo-name{font-weight:700;font-size:13px;color:var(--ink);white-space:nowrap}
.logo.light .logo-mark{background:#fff}
.logo.light .logo-name{color:#fff}
.small{font-size:6px;color:var(--muted);line-height:1.5;white-space:nowrap}

/* business cards */
.card{width:218px;height:125px;border-radius:4px}
.card-white{padding:16px 14px}
.card-white .person{position:absolute;left:40px;top:62px;font-size:8px;font-weight:600}
.card-white .person span{display:block;font-weight:400;color:var(--muted);font-size:6px}
.card-white .contacts{position:absolute;left:106px;top:40px;font-size:6px;line-height:1.6;color:var(--ink);white-space:nowrap}
.card-white .contacts b{display:inline-block;width:24px;font-weight:600}
.card-white .line{position:absolute;left:100px;top:38px;width:1px;height:48px;background:var(--rule)}
.card-color{display:flex;flex-direction:column;align-items:center;justify-content:center;gap:8px;color:#fff}
.card-color .logo-name{font-size:16px}
.card-color .logo-mark{width:18px;height:18px}
.card-color .small{color:rgba(255,255,255,.85);text-align:center}
.card-blue{background:radial-gradient(circle at 40% 40%,#3aa2ec,var(--blue-dark))}
.card-orange{background:linear-gradient(135deg,var(--yellow),var(--orange))}
.card-green{background:radial-gradient(circle at 40% 40%,#86c95a,var(--green-dark))}

/* letterhead & fax */
.sheet{width:245px;height:389px;padding:14px 16px}
.sheet .footer{position:absolute;left:16px;right:16px;bottom:12px;border-top:1px solid var(--rule);padding-top:4px;font-size:5px;color:var(--muted);white-space:nowrap;overflow:hidden}
.fax .title{position:absolute;right:16px;top:38px;font-size:13px;font-weight:700;color:var(--ink)}
.fax .fields{margin-top:40px;display:grid;grid-template-columns:1fr 1fr;column-gap:12px;row-gap:7px}
.fax .field{font-size:6px;font-weight:600;border-bottom:1px solid var(--rule);padding-bottom:2px}
.fax .checks{display:flex;gap:6px;margin-top:12px;font-size:5px;color:var(--muted);white-space:nowrap}
.fax .checks span::before{content:"";display:inline-block;width:5px;height:5px;border:1px solid var(--muted);margin-right:2px;vertical-align:-1px}
.fax .footer{background:var(--black);color:#ddd;border:none;padding:3px 5px}

/* DL envelope */
.envelope{width:298px;height:140px;padding:12px 14px}
.envelope .addr{margin-top:3px}
.envelope .window{position:absolute;left:28px;bottom:22px;width:120px;height:36px;border:1px solid var(--rule);border-radius:3px}

/* tall envelope set */
.envelope-set{width:346px;height:576px;padding:16px 18px;overflow:hidden}
.envelope-set .addr{margin-top:3px}
.envelope-set .band{position:absolute;left:0;right:0;top:146px;height:14px;background:var(--black);color:#ddd;font-size:5.5px;padding:3px 12px;white-space:nowrap}
.envelope-set svg{position:absolute;left:0;top:160px}
</style>
</head>
<body>

<!-- business cards -->
<div class="item card card-white" style="left:29px;top:24px">
  <div class="logo"><span class="logo-mark"></span><span class="logo-name">CopperWagon</span></div>
  <div class="person">Leo Harwick<span>Director</span></div>
  <div class="line"></div>
  <div class="contacts"><b>Phone:</b>07 3100 2480<br><b>Fax:</b>07 3100 2481<br><b>Mobile:</b>0412 558 903<br><b>Email:</b>hello@copperwagon.com.au<br><b>Web:</b>www.copperwagon.com.au</div>
</div>
<div class="item card card-white" style="left:29px;top:178px">
  <div class="logo"><span class="logo-mark"></span><span class="logo-name">CopperWagon</span></div>
  <div class="person">Leo Harwick<span>Director</span></div>
  <div class="line"></div>
  <div class="contacts"><b>Phone:</b>07 3100 2480<br><b>Fax:</b>07 3100 2481<br><b>Email:</b>hello@copperwagon.com.au<br><b>Web:</b>www.copperwagon.com.au</div>
</div>
<div class="item card card-color card-blue" style="left:29px;top:322px">
  <div class="logo light"><span class="logo-mark"></span><span class="logo-name">CopperWagon</span></div>
  <div class="small">12 Harbour Street, Suite 4<br>Brisbane QLD 4000</div>
</div>
<div class="item card card-color card-orange" style="left:29px;top:466px">
  <div class="logo light"><span class="logo-mark"></span><span class="logo-name">CopperWagon</span></div>
  <div class="small">www.copperwagon.com.au</div>
</div>
<div class="item card card-color card-green" style="left:264px;top:466px">
  <div class="logo light"><span class="logo-mark"></span><span class="logo-name">CopperWagon</span></div>
  <div class="small">www.copperwagon.com.au</div>
</div>

<!-- letterhead -->
<div class="item sheet" style="left:264px;top:24px">
  <div class="logo"><span class="logo-mark"></span><span class="logo-name">CopperWagon</span></div>
  <div class="footer">12 Harbour St, Brisbane QLD 4000 &nbsp;|&nbsp; www.copperwagon.com.au &nbsp;|&nbsp; Ph: 07 3100 2480</div>
</div>

<!-- fax -->
<div class="item sheet fax" style="left:542px;top:24px">
  <div class="logo"><span class="logo-mark"></span><span class="logo-name">CopperWagon</span></div>
  <div class="title">FAX</div>
  <div class="fields">
    <div class="field">To:</div><div class="field">From:</div>
    <div class="field">Fax:</div><div class="field">Pages:</div>
    <div class="field">Phone:</div><div class="field">Date:</div>
    <div class="field">Re:</div><div class="field">CC:</div>
  </div>
  <div class="checks"><span>Urgent</span><span>For Review</span><span>Please Comment</span><span>Please Reply</span></div>
  <div class="footer">Web: www.copperwagon.com.au &nbsp;|&nbsp; Contact #: 07 3100 2480</div>
</div>

<!-- DL envelope -->
<div class="item envelope" style="left:499px;top:446px">
  <div class="logo"><span class="logo-mark"></span><span class="logo-name">CopperWagon</span></div>
  <div class="small addr">12 Harbour Street, Suite 4, Brisbane QLD 4000</div>
  <div class="window"></div>
</div>

<!-- envelope set -->
<div class="item envelope-set" style="left:830px;top:24px">
  <div class="logo"><span class="logo-mark"></span><span class="logo-name">CopperWagon</span></div>
  <div class="small addr">12 Harbour Street, Suite 4, Brisbane QLD 4000</div>
  <div class="band">Web: www.copperwagon.com.au &nbsp;|&nbsp; Contact #: 07 3100 2480</div>
  <svg width="346" height="416" viewBox="0 0 346 416" font-family="Open Sans, Arial, sans-serif" font-weight="700" font-size="10">
    <g>
      <rect x="0" y="0" width="346" height="110" fill="#fff"/>
      <path d="M0 0H346V18L173 60L0 18Z" fill="#1c1c1c"/>
      <rect x="132" y="20" width="10" height="10" rx="2" fill="#fff"/>
      <text x="146" y="29" fill="#fff">CopperWagon</text>
    </g>
    <g transform="translate(0,72)">
      <rect x="0" y="0" width="346" height="110" fill="#fff" stroke="#ddd"/>
      <path d="M0 0H346V18L173 60L0 18Z" fill="#fff" stroke="#bbb"/>
      <rect x="132" y="20" width="10" height="10" rx="2" fill="#1f7fd0"/>
      <text x="146" y="29" fill="#3a3a3a">CopperWagon</text>
    </g>
    <g transform="translate(0,144)">
      <rect x="0" y="0" width="346" height="110" fill="#fff"/>
      <path d="M0 0H346V18L173 60L0 18Z" fill="#1f7fd0"/>
      <rect x="132" y="20" width="10" height="10" rx="2" fill="#fff"/>
      <text x="146" y="29" fill="#fff">CopperWagon</text>
    </g>
    <g transform="translate(0,216)">
      <rect x="0" y="0" width="346" height="110" fill="#fff"/>
      <path d="M0 0H346V18L173 60L0 18Z" fill="#f07f12"/>
      <rect x="132" y="20" width="10" height="10" rx="2" fill="#fff"/>
      <text x="146" y="29" fill="#fff">CopperWagon</text>
    </g>
    <g transform="translate(0,288)">
      <rect x="0" y="0" width="346" height="128" fill="#fff"/>
      <path d="M0 0H346V18L173 60L0 18Z" fill="#6cb33f"/>
      <rect x="132" y="20" width="10" height="10" rx="2" fill="#fff"/>
      <text x="146" y="29" fill="#fff">CopperWagon</text>
    </g>
  </svg>
</div>

</body>
</html>
```